CREW VORTEX Martials Arts Gym - DL Flyer Design to launch their new location!!

We need a 1 sided DL flyer design (in landscape) for a martial arts gym with a world class facility specialising in Kickboxing, Muay Thai, MMA, Boxing, Ladies Classes and Kids Classes. More info may be obtained at www.vortexbrindale.com.au

The design should communicate who we are / what we do

This flyer will be distributed to 10,000 houses within a 10km radius of the gym

Target Market(s)

*Our target market is males aged 20 - 30 who are looking for a challenging training regime (sick and tired of the boring old treadmill)

*Should also be family friendly for mothers and kids wishing to join our gym

Industry/Entity Type

Gym

Requirements
Must have
• *Flyer must demonstrate who we are / what we do (gaining awareness, these flyers will be distributed to 10,000 homes within a 10km radius)
• *Must include an incentive coupon offer - FREE CLASS PASS or something of the likes.
• *Must include our partner logos Novaro / Kelvoro / Global Striking Federation / Striking Sports Oceania and GPBF (all logos have been provided)
• *Web address / Address / Contact number / Chatterly Icon
• W: www.vortexbrindale.com.au
• A: 42 Tarrant Lane, Brindale VIC 3094
• C: (03) 9627 5180
• *Images have been provided of the gym and some of our members during classes (more information may be gained at our website www.vortexbrindale.com.au)
Nice to have
• *Colours preferred but NOT essential are splashes of blue & red combination (boxing ring corner colours)

```html
<!DOCTYPE html>
<html lang="en">
<head>
<meta charset="utf-8">
<title>Crew Vortex Gym – DL Flyer</title>
<link rel="stylesheet" href="https://fonts.googleapis.com/css2?family=PT+Sans:wght@400;700&display=swap">
<style>
  :root {
    --bg-deep: #0b0b0d;
    --bg-mid: #1c1d22;
    --blue: #1b9ad8;
    --blue-light: #5cc4f0;
    --blue-dark: #0f6fa8;
    --white: #ffffff;
    --grey-text: #d9d9d9;
    --footer: #2a2a2c;
    --red: #d3262b;
  }
  * { margin: 0; padding: 0; box-sizing: border-box; }
  html, body { width: 1200px; height: 629px; overflow: hidden; background: var(--bg-deep); }
  body { font-family: "PT Sans", Arial, sans-serif; color: var(--white); }

  .flyer {
    position: relative;
    width: 1200px;
    height: 629px;
    overflow: hidden;
    background:
      radial-gradient(ellipse 520px 300px at 560px 330px, rgba(60,62,72,0.85), transparent 70%),
      radial-gradient(ellipse 380px 200px at 250px 330px, rgba(27,154,216,0.22), transparent 75%),
      linear-gradient(180deg, var(--bg-mid) 0%, var(--bg-deep) 100%);
  }

  .photo { position: absolute; }
  .photo--ring {
    left: 0; top: 0; width: 470px; height: 240px;
    background:
      linear-gradient(90deg, rgba(11,11,13,0) 55%, var(--bg-mid) 100%),
      linear-gradient(180deg, rgba(11,11,13,0) 45%, var(--bg-mid) 100%),
      linear-gradient(160deg, #6f6f78 0%, #8a3b3b 35%, #35507a 65%, #2a2e3a 100%);
  }
  .photo--training {
    right: 0; top: 0; width: 360px; height: 210px;
    background:
      linear-gradient(90deg, var(--bg-mid) 0%, rgba(11,11,13,0) 35%),
      linear-gradient(180deg, rgba(11,11,13,0) 70%, rgba(11,11,13,0.6) 100%),
      linear-gradient(150deg, #5a2a2a 0%, #b9a79a 45%, #e4dcd6 70%, #6b3030 100%);
  }
  .photo--kids {
    right: 0; top: 207px; width: 250px; height: 325px;
    background:
      linear-gradient(90deg, var(--bg-mid) 0%, rgba(11,11,13,0) 30%),
      linear-gradient(170deg, #5b3838 0%, #a07d70 30%, #d7cfc9 55%, #3a5a8c 85%, #8e3434 100%);
  }

  .brand {
    position: absolute; left: 318px; top: 60px; width: 567px;
    display: flex; align-items: center; justify-content: center; gap: 16px;
  }
  .brand__dot { width: 26px; height: 26px; border-radius: 50%; background: var(--blue); }
  .brand__name {
    font-weight: 700; font-size: 56px; line-height: 1; color: var(--white); letter-spacing: 1px;
  }

  .headline { position: absolute; left: 83px; top: 222px; }
  .headline__title {
    font-weight: 700; font-size: 50px; line-height: 1; color: var(--blue); letter-spacing: -0.5px;
  }
  .headline__tagline { margin-top: 6px; font-weight: 700; font-size: 23px; color: var(--white); }

  .cta {
    position: absolute; left: 0; top: 341px; width: 453px; height: 71px;
    border-radius: 0 10px 10px 0;
    background: linear-gradient(90deg, var(--blue-dark) 0%, var(--blue) 40%, var(--blue-light) 100%);
    padding: 13px 0 0 83px;
    font-weight: 700; font-size: 19px; line-height: 1.15; text-transform: uppercase;
  }

  .hours { position: absolute; left: 83px; top: 444px; font-size: 14px; line-height: 1.3; }
  .hours__label { color: var(--blue); font-weight: 700; text-transform: uppercase; }

  .coupon {
    position: absolute; left: 345px; top: 436px; width: 270px; height: 78px;
    border: 2px dashed var(--white);
    border-radius: 6px;
    padding: 8px 14px;
    background: rgba(211,38,43,0.18);
  }
  .coupon__title { font-weight: 700; font-size: 22px; line-height: 1.05; color: var(--white); text-transform: uppercase; }
  .coupon__title span { color: var(--red); }
  .coupon__note { margin-top: 4px; font-size: 12.5px; line-height: 1.25; color: var(--grey-text); }

  .info { position: absolute; left: 668px; top: 244px; font-size: 13.5px; line-height: 17px; }
  .info__heading { color: var(--blue); font-weight: 700; text-transform: uppercase; font-size: 13.5px; }
  .info__list { list-style: none; margin-bottom: 14px; }
  .info__list li::before { content: "· "; }
  .info__list .indent::before { content: ""; padding-left: 12px; }

  .footer {
    position: absolute; left: 0; top: 532px; width: 1200px; height: 97px;
    background: var(--footer);
  }
  .footer__address {
    position: absolute; left: 83px; top: 14px; font-size: 15px; line-height: 1.3;
    color: var(--grey-text); font-style: normal;
  }
  .social {
    position: absolute; left: 397px; top: 26px; display: flex; gap: 16px; align-items: center;
  }
  .social__item { display: flex; align-items: center; gap: 6px; font-size: 13px; font-weight: 700; }
  .social__mark { width: 14px; height: 14px; background: var(--white); }
  .web {
    position: absolute; left: 397px; top: 52px; font-size: 15px; font-weight: 700; color: var(--blue);
  }

  .partners {
    position: absolute; left: 740px; top: 22px; width: 420px; height: 56px;
    display: flex; align-items: center; justify-content: space-between;
  }
  .partner-name { font-size: 17px; font-weight: 700; color: var(--white); }
  .partner-badge { width: 52px; height: 52px; border-radius: 50%; background: #4b5c86; }
  .partner-badge--square { border-radius: 6px; background: #5a2d3b; }
</style>
</head>
<body>
<main class="flyer">
  <div class="photo photo--ring" role="img" aria-label="Gym interior with competition boxing ring and matted floor"></div>
  <div class="photo photo--training" role="img" aria-label="Member training on a punching bag"></div>
  <div class="photo photo--kids" role="img" aria-label="Kids practising boxing stance on the mats"></div>

  <div class="brand">
    <span class="brand__dot"></span>
    <span class="brand__name">CREW VORTEX</span>
  </div>

  <header class="headline">
    <h1 class="headline__title">Crew Vortex Gym</h1>
    <p class="headline__tagline">A boxing gym without the attitude.</p>
  </header>

  <div class="cta">Call us today on 03 9627 5180<br>to get started</div>

  <section class="hours">
    <p class="hours__label">Trading Hours</p>
    <p>Mon - Thurs (3.30pm - 9.00pm)</p>
    <p>Saturday (9.30am - 2.00pm)</p>
  </section>

  <section class="coupon">
    <p class="coupon__title"><span>Free</span> Class Pass</p>
    <p class="coupon__note">Bring this flyer in for one free class.<br>New members only. One per person.</p>
  </section>

  <section class="info">
    <h2 class="info__heading">Training Facilities</h2>
    <ul class="info__list">
      <li>Competition Size Boxing Ring</li>
      <li>Matted Training Area Approx 250m2</li>
      <li>Fully equipped weights area</li>
      <li>Cardio Equipment</li>
      <li>Punching Bags</li>
      <li>Speed Balls</li>
    </ul>
    <h2 class="info__heading">Training Offered</h2>
    <ul class="info__list">
      <li>Boxing, Kickboxing &amp; Muay Thai Classes</li>
      <li class="indent">- members only</li>
      <li>Fitness/Circuit Training Classes</li>
      <li>Sparring Sessions</li>
      <li>Female Only Classes</li>
      <li>Kids Only Classes</li>
      <li>Personal Training (one-on-one &amp; group)</li>
    </ul>
  </section>

  <footer class="footer">
    <address class="footer__address">
      42 Tarrant Lane (enter via Marlow St),<br>
      Brindale, VIC 3094,<br>
      info@vortexbrindale.com.au
    </address>
    <div class="social">
      <span class="social__item"><span class="social__mark"></span>Chatterly</span>
      <span class="social__item"><span class="social__mark"></span>Chirpline</span>
      <span class="social__item"><span class="social__mark"></span>Linkwell</span>
    </div>
    <p class="web">www.vortexbrindale.com.au</p>
    <div class="partners">
      <span class="partner-name">Novaro</span>
      <span class="partner-badge" role="img" aria-label="GPBF partner badge"></span>
      <span class="partner-name">Kelvoro</span>
      <span class="partner-badge partner-badge--square" role="img" aria-label="Striking Sports Oceania partner badge"></span>
    </div>
  </footer>
</main>
</body>
</html>
```